Restaurant needs take out menu design

I need a takeout menu design for a new restaurant. We will be printing via inkharbor.com. On their website, you can download blank templates.

See specs:
1. 11x17 accordion folding. http://www.inkharbor.com/take-out-menu-printing.html
2. Font is Times New Roman
3. All design/font on the menu will be black

*See menu inspiration attached. Feel free to reuse similar boarders and design.
*Attached is our logo
*Please let me know if any other information is needed.
*Attached is a our menu with prices.
*Please send to me in an ai file.

Industry/Entity Type

Restaurant

Font styles to use
Serif
Decorative

Requirements
Must have
• new times roman. black lettering
• all uppercase lettering
• must be in adobe illustrator format
• have the same feel as the menus I attached
Nice to have
• Leave the area for the telephone numbers, hours, address and business hours the same as the copy and pasted menu.
Should not have
• No other color than black

```html
<!DOCTYPE html>
<html lang="en">
<head>
<meta charset="utf-8">
<title>The Jade Court – Take Out Menu</title>
<link href="https://fonts.googleapis.com/css2?family=Tinos:ital,wght@0,400;0,700;1,400&display=swap" rel="stylesheet">
<style>
:root{
  --ink:#111;
  --paper:#fff;
  --ground:#e6e2dc;
  --ornament:#c9c9c9;
  --spicy:#b10000;
}
*{box-sizing:border-box;margin:0;padding:0}
html,body{width:1037px;height:1200px;overflow:hidden;background:var(--ground)}
body{position:relative;font-family:"Tinos","Times New Roman",serif;color:var(--ink);text-transform:uppercase}
.sheet{position:absolute;background:var(--paper);display:grid;grid-template-columns:repeat(4,1fr);box-shadow:0 2px 6px rgba(0,0,0,.25)}
.sheet--outside{left:26px;top:24px;width:984px;height:562px;padding:12px 14px;gap:14px}
.sheet--inside{left:122px;top:592px;width:907px;height:580px;padding:14px 14px;gap:12px}
.panel{border:1px solid var(--ink);outline:1px solid var(--ink);outline-offset:-4px;padding:14px 14px;overflow:hidden;font-size:6.6px;line-height:8.2px}
.cover{display:flex;flex-direction:column;align-items:center;justify-content:space-between;padding:30px 18px}
.ornament{width:150px;height:120px;background:radial-gradient(ellipse at center,var(--ornament),rgba(255,255,255,0) 70%)}
.brand{border:2px solid var(--ink);padding:10px 14px;text-align:center;width:100%;font-weight:400}
.brand span{display:block;letter-spacing:6px;font-size:14px;line-height:18px}
.brand strong{display:block;font-weight:400;font-size:34px;line-height:36px;letter-spacing:1px}
.item{display:flex}
.item .name{flex:1}
.item .pt,.item .qt{width:28px;text-align:right}
.desc{font-style:italic;text-transform:none}
.market{text-transform:none}
.head{text-align:center;font-weight:700;margin:6px 0 2px}
.gap{height:7px}
.center{text-align:center}
.small-caps{text-align:center;font-size:6px}
.rule{width:40px;height:1px;background:var(--ink);margin:5px auto}
.spicy{color:var(--spicy)}
.entry{margin-bottom:6px}
</style>
</head>
<body>

<section class="sheet sheet--outside">
  <div class="panel cover">
    <div class="ornament" role="img" aria-label="Grey floral flourish decoration"></div>
    <div class="brand"><span>THE</span><strong>JADE</strong><span>COURT</span></div>
    <div class="ornament" role="img" aria-label="Grey floral vine decoration"></div>
  </div>

  <div class="panel">
    <div class="item"><span class="name">PEKING DUCK</span><span>(H) 19.95 &nbsp;(F) 34.95</span></div>
    <p class="desc">This turnover roasted duck is served best at human taste. The skin and meat are skillfully carved and are served with scallions, hoisin sauce and pancakes.</p>
    <div class="gap"></div>
    <p>VEGETABLES</p>
    <p>FILLER 1- TBD</p><p>FILLER 2- TBD</p><p>FILLER 3- TBD</p><p>FILLER 4- TBD</p><p>FILLER 5 -TBD</p>
    <div class="item"><span class="name">MOO SHU VEGETABLES</span><span>11.95</span></div>
    <div class="item"><span class="name">DRIED SAUTEED STRING BEANS</span><span>11.95</span></div>
    <div class="item"><span class="name">SAUTEED BROCCOLI IN GARLIC SAUCE</span><span>11.95</span></div>
    <div class="item"><span class="name">EGGPLANT IN GARLIC SAUCE</span><span>11.95</span></div>
    <div class="item"><span class="name">MIXED VEGETABLES IN BROWN SAUCE</span><span>11.95</span></div>
    <p>EVER GREEN IN LIGHT FRESH</p>
    <div class="item"><span class="name">GARLIC SAUCE</span><span>11.95</span></div>
    <p class="desc">(Broccoli, String Beans, Asparagus And Snow Peas)</p>
    <div class="item"><span class="name">SOFT BEAN CURD CASSEROLE</span><span>11.95</span></div>
    <div class="item"><span class="name">SAUTEED SHANGHAI BOK CHOY</span><span>11.95</span></div>
    <div class="item"><span class="name">BEAN CURD WITH MIXED VEGETABLES</span><span>12.75</span></div>
    <div class="item"><span class="name">GENERAL TSO'S BEAN CURD</span><span>12.95</span></div>
    <div class="gap"></div>
    <div class="item"><span class="name">SIDE ORDERS</span><span class="pt">PT.</span><span class="qt">QT.</span></div>
    <div class="item"><span class="name">PANCAKE (1)</span><span class="qt">0.50</span></div>
    <div class="item"><span class="name">FRESH CRISPY NOODLES</span><span class="qt">1.50</span></div>
    <div class="item"><span class="name">CANNED SODA</span><span class="qt">1.50</span></div>
    <div class="item"><span class="name">WHITE RICE</span><span class="pt">1.75</span><span class="qt">3.00</span></div>
    <div class="item"><span class="name">BROWN RICE</span><span class="pt">2.25</span><span class="qt">4.00</span></div>
    <div class="item"><span class="name">FRIED RICE <i class="desc">(Chicken, Pork, Or Vegetable)</i></span><span class="pt">6.95</span><span class="qt">8.95</span></div>
    <div class="item"><span class="name">FRIED RICE <i class="desc">(Beef or Shrimp)</i></span><span class="pt">8.95</span><span class="qt">9.95</span></div>
    <div class="item"><span class="name">HOUSE SPECIAL FRIED RICE</span><span class="pt">8.95</span><span class="qt">9.95</span></div>
    <p>**BROWN RICE AVAILABLE UPON REQUEST FOR AN EXTRA CHARGE <span style="float:right">1.00</span></p>
    <div class="item"><span class="name">LO MEIN <i class="desc">(Chicken, Pork, or Vegetable)</i></span><span class="pt">7.95</span><span class="qt">9.95</span></div>
    <div class="item"><span class="name">LO MEIN <i class="desc">(Beef or Shrimp)</i></span><span class="pt">8.95</span><span class="qt">10.95</span></div>
    <div class="item"><span class="name">HOUSE SPECIAL LO MEIN</span><span class="pt">10.50</span><span class="qt">12.50</span></div>
    <div class="item"><span class="name">CHOW MEIN <i class="desc">(Chicken, Pork, Beef, Shrimp, Vegetable, or House)</i></span><span class="qt">9.95</span></div>
    <div class="item"><span class="name">CHOW FUN NOODLES <i class="desc">(Chicken, Pork, Beef, Shrimp, Vegetable, or House)</i></span><span class="qt">9.95</span></div>
    <div class="item"><span class="name">MEI FUN NOODLES <i class="desc">(Chicken, Pork, Beef, Shrimp, Vegetable, or House)</i></span><span class="qt">9.95</span></div>
    <div class="item"><span class="name">CURRY MEI FUN SINGAPORE STYLE WITH EGG</span><span class="qt">12.95</span></div>
    <div class="item"><span class="name">CANTONESE PAN FRIED NOODLES</span><span class="qt">16.95</span></div>
    <p class="desc">(Crispy Egg Noodles with Chicken, Pork, Shrimp, Mushrooms and Vegetables in a Delicate White Sauce)</p>
    <p class="head">TRADITIONAL CHINESE DISHES<br>APPETIZERS</p>
    <div class="item"><span class="name">CHILLED SEAWEED IN SEASONED GARLIC</span><span>4.50</span></div>
    <div class="item"><span class="name">CHILLED SWEET CABBAGE</span><span>4.50</span></div>
    <div class="item"><span class="name">FRESH CUCUMBER IN SEASONED GARLIC</span><span>4.95</span></div>
    <div class="item"><span class="name">DAN DAN NOODLE</span><span>6.50</span></div>
    <p class="desc">(Egg Noodles in Our Delicious Hot Peanut Sesame Sauce)</p>
    <p>BEEF TENDON AND TRIPE IN A HOT SZECHUAN</p>
  </div>

  <div class="panel">
    <div class="item"><span class="name">PEPPER SAUCE</span><span>7.95</span></div>
    <div class="item"><span class="name">BANG BANG CHICKEN</span><span>7.95</span></div>
    <p class="desc">(Shredded Chicken with A Hot Peanut Sesame Sauce) (Served Chilled)</p>
    <div class="item"><span class="name">SPICY SHRIMP IN HOT OIL</span><span>7.95</span></div>
    <p class="head">ENTREES</p>
    <div class="item"><span class="name">SAUTEED RICE CAKE</span><span>12.95</span></div>
    <p class="desc">(Chewy Rice Cake Sauteed With Bok Choy and Shredded Pork)</p>
    <div class="item"><span class="name">"ANTS ON A TREE"</span><span>12.95</span></div>
    <p class="desc">(Clear Vermicelli Noodles with Minced Pork Sauteed in a Spicy Sauce)</p>
    <p>SOFT BEAN CURD CASSEROLE IN</p>
    <div class="item"><span class="name">BROWN SAUCE</span><span>12.95</span></div>
    <p>BEAN CURD HUNAN STYLE WITH MINCED PORK</p>
    <div class="item"><span class="name desc">(Ma Po Tofu)</span><span>12.95</span></div>
    <div class="item"><span class="name">SPICY BEEF WITH HOT PEPPERS</span><span>15.95</span></div>
    <p class="desc">(Shredded Beef with Hot Chili Peppers)</p>
    <p>SICHUAN BOILED STEW IN A FIRE</p>
    <div class="item"><span class="name">HOT OIL SAUCE</span><span>17.95</span></div>
    <p class="desc">(Beef, Chicken, Fish) (A Classic Tongue-Burning Dish Served Best at Hunan Taste)</p>
    <div class="item"><span class="name">SALT PEPPER SHRIMP WITH SCALLIONS</span><span>19.95</span></div>
    <div class="item"><span class="name">SEA CUCUMBER</span><span>28.50</span></div>
    <p class="desc">(Sauteed with Vegetables in a Brown Sauce)</p>
    <div class="rule"></div>
    <p class="head">LUNCH SPECIALS</p>
    <p class="center">SERVED FROM 11:30 AM – 3:00PM<br>MONDAY – FRIDAY (EXCLUDING HOLIDAYS)<br>WITH A CHOICE OF SOUP: WONTON, EGG DROP, OR HOT &amp; SOUR SOUP (EXCEPT NOODLE SOUP)<br>WITH A CHOICE OF RICE: WHITE RICE, BROWN RICE, OR VEGETABLE FRIED RICE<br>EGG ROLL OR SHRIMP ROLL $2.00 EXTRA</p>
    <p class="head">$8.75</p>
    <p class="small-caps">BEAN CURD WITH MIXED VEGETABLES<br>SAUTEED MIXED VEGETABLES<br>BROCCOLI IN GARLIC SAUCE<br>DRIED SAUTEED STRING BEANS<br>LO MEIN WITH ROAST PORK, CHICKEN, BEEF, OR SHRIMP<br>CHOW MEIN WITH ROAST PORK, CHICKEN, BEEF, OR SHRIMP</p>
    <p class="head">$8.95</p>
    <p class="small-caps">CHICKEN, BEEF, PORK, OR BABY SHRIMP</p>
    <p class="desc center">With a choice of broccoli, string beans, or mixed vegetables and a choice of brown sauce, garlic sauce, black bean sauce or white sauce</p>
    <p class="small-caps">SWEET &amp; SOUR CHICKEN OR PORK<br>PEPPER STEAK WITH ONIONS<br>SAUTEED SHREDDED BEEF WITH HOT SAUCE<br>CHICKEN WITH CASHEW NUTS</p>
    <p class="head">$9.25</p>
    <p class="small-caps">SESAME CHICKEN<br>GENERAL TSO'S CHICKEN</p>
  </div>

  <div class="panel">
    <p class="small-caps">TANGERINE CHICKEN<br>GOLDEN ORCHARD CHICKEN<br>SESAME BEEF<br>TANGERINE BEEF<br>PEKING PORK CHOPS<br>MANDARIN PORK CHOPS<br>TRIPLE CROWN<br>BEEF NOODLE SOUP<br>PORK CHOP NOODLE SOUP<br>TEN INGREDIENTS NOODLE SOUP</p>
    <p class="desc center">(Chicken, Pork, Shrimp, and Mixed Vegetables in a Chicken Broth)</p>
    <p class="small-caps">DAN DAN NOODLES <i class="desc">(Peanut Sesame Noodles)</i><br>PEKING NOODLES</p>
    <p class="desc center">(Minced Pork, Bean Curd, and Bamboo in a Brown Hoisin Sauce)</p>
    <div class="rule"></div>
    <p class="head">$10.95</p>
    <p class="small-caps">JUMBO SHRIMP WITH BROCCOLI<br>JUMBO SHRIMP WITH MIXED VEGETABLES<br>SHRIMP WITH LOBSTER SAUCE<br>KUNG PO SHRIMP WITH PEANUTS<br>SAUTEED TWO DELICACIES<br>SCALLOP WITH MIXED VEGETABLES<br>SCALLOPS WITH GARLIC SAUCE</p>
    <div class="rule"></div>
    <p class="head">$11.50</p>
    <p class="small-caps">CRISPY SHRIMP<br>GENERAL TSO'S SHRIMP<br>HUNAN SHRIMP WITH WALNUTS<br>GOLDEN ORCHARD SHRIMP<br>SEAFOOD SUPREME<br>HAPPY FAMILY<br>GENERAL TSO'S TRIPLE FRAGRANCE</p>
    <div class="rule"></div>
    <div class="gap"></div>
    <p><span class="spicy">&#8221;</span> HOT &amp; SPICY<br>WE CAN ALTER THE SPICINESS ACCORDING TO YOUR TASTE<br>CRISPY NOODLES ONLY COME WITH SOUP OR CHOW MEIN<br>ADDITIONAL SAUCE ON THE SIDE- EXTRA CHARGE $2.00</p>
  </div>
</section>

<section class="sheet sheet--inside">
  <div class="panel">
    <div class="item"><b class="name">SOUPS</b><span class="pt">PT.</span><span class="qt">QT.</span></div>
    <div class="item"><span class="name">EGG DROP SOUP</span><span class="pt">2.75</span><span class="qt">4.95</span></div>
    <div class="item"><span class="name">HOT &amp; SOUR SOUP</span><span class="pt">3.95</span><span class="qt">6.75</span></div>
    <div class="item"><span class="name">WONTON SOUP</span><span class="pt">3.95</span><span class="qt">6.75</span></div>
    <p>BEAN CURD SOUP WITH</p>
    <div class="item"><span class="name">VEGETABLES (2)</span><span class="qt">6.95</span></div>
    <div class="item"><span class="name">CHICKEN CORN SOUP (2)</span><span class="qt">7.95</span></div>
    <div class="item"><span class="name">TEN INGREDIENTS RICE SOUP (2)</span><span class="qt">7.95</span></div>
    <div class="item"><span class="name">SYMPHONY SEAFOOD SOUP (FOR 2)</span><span class="qt">12.95</span></div>
    <p class="head">APPETIZERS</p>
    <div class="item"><span class="name">VEGETABLE ROLL</span><span>2.25</span></div>
    <div class="item"><span class="name">EGG ROLL</span><span>2.50</span></div>
    <div class="item"><span class="name">SHRIMP ROLL</span><span>2.50</span></div>
    <div class="item"><span class="name">STEAMED EDAMAME</span><span>3.95</span></div>
    <div class="item"><span class="name">SCALLION PANCAKES</span><span>4.50</span></div>
    <div class="item"><span class="name">COLD NOODLES IN SESAME SAUCE</span><span>4.95</span></div>
    <div class="item"><span class="name">CRISPY CRAB RAGOON (3)</span><span>4.95</span></div>
    <div class="item"><span class="name">SHRIMP TOAST (4)</span><span>5.75</span></div>
    <div class="item"><span class="name">BARBECUED BEEF STICKS (2)</span><span>5.95</span></div>
    <div class="item"><span class="name">STEAMED DUMPLINGS (6)</span><span>6.50</span></div>
    <div class="item"><span class="name">PAN FRIED DUMPLINGS (6)</span><span>6.50</span></div>
    <p>DUMPLINGS WITH HOT OIL</p>
    <div class="item"><span class="name desc">(Peanut Sesame Sauce) (6)</span><span>6.50</span></div>
    <div class="item"><span class="name">SPICY CHICKEN DUMPLINGS (10)</span><span>6.50</span></div>
    <div class="item"><span class="name">STEAMED EDAMAME DUMPLINGS (6)</span><span>6.50</span></div>
    <div class="item"><span class="name">STEAMED SHRIMP DUMPLINGS (4)</span><span>6.50</span></div>
    <div class="item"><span class="name">SIU MAI DUMPLINGS (4)</span><span>6.50</span></div>
    <div class="item"><span class="name">VEGETABLE DUMPLINGS (6)</span><span>6.50</span></div>
    <p>THREE KINDS OF DUMPLINGS</p>
    <div class="item"><span class="name desc">(Pork, Vegetable and Shrimp)</span><span>6.95</span></div>
    <div class="item"><span class="name">BONELESS RIBS</span><span>7.95</span></div>
    <div class="item"><span class="name">BACON SHRIMP ROLLS (6)</span><span>8.50</span></div>
    <div class="item"><span class="name">BARBECUED SPARE RIBS</span><span>(4) 9.95 &nbsp;(8) 15.95</span></div>
    <div class="item"><span class="name">PU PU PLATTER (FOR 2)</span><span>16.95</span></div>
    <p class="desc">Shrimp Toast, BBQ Spare Ribs, Beef Sticks, Shrimp Rolls, Siu Mai Dumplings, and Fried Dumplings</p>
    <p class="head">CHICKEN</p>
    <div class="item"><span class="name">MOO SHU CHICKEN</span><span>13.50</span></div>
    <div class="item"><span class="name">CHICKEN WITH BROCCOLI</span><span>13.50</span></div>
    <div class="item"><span class="name">CHICKEN WITH MIXED VEGETABLES</span><span>13.50</span></div>
    <div class="item"><span class="name">CHICKEN WITH CASHEW NUTS</span><span>13.50</span></div>
    <div class="item"><span class="name">KUNG PO CHICKEN WITH PEANUTS</span><span>13.50</span></div>
    <div class="item"><span class="name">CHICKEN IN GARLIC SAUCE</span><span>13.50</span></div>
    <div class="item"><span class="name">CHICKEN WITH STRING BEANS</span><span>13.50</span></div>
    <div class="item"><span class="name">SWEET &amp; SOUR CHICKEN</span><span>13.50</span></div>
    <div class="item"><span class="name">CHICKEN WITH EGGPLANT</span><span>13.50</span></div>
    <div class="item"><span class="name">HUNAN CHICKEN WITH BLACK BEAN SAUCE</span><span>13.95</span></div>
    <div class="item"><span class="name">CHICKEN WITH SNOW PEAS</span><span>13.95</span></div>
    <div class="item"><span class="name">CHICKEN WITH ASPARAGUS</span><span>13.95</span></div>
    <div class="item"><span class="name">PEPPERCORN CHICKEN</span><span>13.95</span></div>
    <p class="head">PORK</p>
    <div class="item"><span class="name">SWEET &amp; SOUR PORK</span><span>12.95</span></div>
    <div class="item"><span class="name">PORK IN GARLIC SAUCE</span><span>12.95</span></div>
    <div class="item"><span class="name">SLICED PORK WITH MIXED VEGETABLES</span><span>12.95</span></div>
    <div class="item"><span class="name">SLICED PORK WITH STRING BEANS</span><span>12.95</span></div>
  </div>

  <div class="panel">
    <div class="item"><span class="name">MOO SHU PORK</span><span>12.95</span></div>
    <p class="head">BEEF</p>
    <div class="item"><span class="name">BEEF WITH BROCCOLI</span><span>14.95</span></div>
    <div class="item"><span class="name">BEEF WITH SNOW PEAS</span><span>14.95</span></div>
    <div class="item"><span class="name">PEPPER STEAK WITH ONIONS</span><span>14.95</span></div>
    <div class="item"><span class="name">SAUTEED SHREDDED HOT BEEF</span><span>14.95</span></div>
    <div class="item"><span class="name">BEEF WITH MIXED VEGETABLES</span><span>14.95</span></div>
    <div class="item"><span class="name">BEEF IN GARLIC SAUCE</span><span>14.95</span></div>
    <div class="item"><span class="name">BEEF WITH SCALLIONS</span><span>14.95</span></div>
    <div class="item"><span class="name">BEEF WITH ASPARAGUS</span><span>14.95</span></div>
    <p class="head">FISH</p>
    <div class="entry"><div class="item"><span class="name">WHOLE FISH</span><span class="market">@Market Price</span></div><p class="desc">Steamed, Crispy, Hunan Style</p></div>
    <div class="entry"><div class="item"><span class="name">FLOUNDER DRAGON BOAT</span><span class="market">@Market Price</span></div><p class="desc">Sliced Filet of Flounder Sautéed with Mixed Vegetables in a Delicate Ginger Scallion Sauce Served Over a Crispy Fishbone</p></div>
    <div class="entry"><div class="item"><span class="name">HEAVENLY FISH</span><span class="market">@Market Price</span></div><p class="desc">Steamed Chilean Sea Bass Steak with a Choice of Ginger Scallion Sauce or Black Bean Sauce</p></div>
    <div class="entry"><div class="item"><span class="name">CRISPY CHILEAN SEA BASS</span><span class="market">@Market Price</span></div><p class="desc">Served with Fresh Scallions</p></div>
    <p class="head">SEAFOOD</p>
    <div class="item"><span class="name">MOO SHU SHRIMP <i class="desc">(with 4 Pancakes)</i></span><span>15.95</span></div>
    <div class="item"><span class="name">SHRIMP WITH BROCCOLI</span><span>17.50</span></div>
    <div class="item"><span class="name">SHRIMP WITH MIXED VEGETABLES</span><span>17.50</span></div>
    <div class="item"><span class="name">SHRIMP IN LOBSTER SAUCE</span><span>17.50</span></div>
    <div class="item"><span class="name">SHRIMP IN BLACK BEAN SAUCE</span><span>17.50</span></div>
    <div class="item"><span class="name">SHRIMP IN GARLIC SAUCE</span><span>17.50</span></div>
    <div class="item"><span class="name">KUNG PO SHRIMP WITH PEANUTS</span><span>17.50</span></div>
    <div class="item"><span class="name">SHRIMP WITH ASPARAGUS</span><span>17.95</span></div>
    <div class="item"><span class="name">SCALLOPS IN GARLIC SAUCE</span><span>17.95</span></div>
    <div class="item"><span class="name">SCALLOPS WITH MIXED VEGETABLES</span><span>17.95</span></div>
    <p class="head">HOUSE SPECIALTIES</p>
    <div class="entry"><div class="item"><span class="name">BASIL CHICKEN</span><span>15.50</span></div><p class="desc">Chunks of dark meat chicken sautéed in a delicious basil sauce with fresh ginger and garlic.</p></div>
    <div class="entry"><div class="item"><span class="name">SESAME CHICKEN</span><span>15.50</span></div><p class="desc">Crispy chunks of chicken sautéed in a sweet brown sauce with a shower of sesame seeds.</p></div>
    <div class="entry"><div class="item"><span class="name">GENERAL TSO'S CHICKEN</span><span>15.50</span></div><p class="desc">Crispy chicken sautéed in our tangy general tso's sauce.</p></div>
    <div class="entry"><div class="item"><span class="name">TANGERINE CHICKEN</span><span>15.50</span></div><p class="desc">Crispy chunks of chicken sautéed in a tangerine flavored spicy sauce.</p></div>
    <div class="entry"><div class="item"><span class="name">IMPERIAL CHICKEN</span><span>15.50</span></div><p class="desc">Chunks of chicken, dry sautéed with three kinds of hot peppers.</p></div>
  </div>

  <div class="panel">
    <div class="entry"><div class="item"><span class="name">PEKING PORK CHOP</span><span>16.95</span></div><p class="desc">Marinated slices of pork chop lightly fried, then sautéed with our special tangy peking sauce.</p></div>
    <div class="entry"><div class="item"><span class="name">MANDARIN PORK CHOP</span><span>16.95</span></div><p class="desc">Crispy slices of pork chop marinated with our chef's special sauce then sautéed with fresh shredded scallions.</p></div>
    <div class="entry"><div class="item"><span class="name">GOLDEN ORCHARD CHICKEN</span><span>16.95</span></div><p class="desc">Crispy white meat chicken sautéed with fresh fruit in a sweet golden orange glaze with cashew nuts.</p></div>
    <div class="entry"><div class="item"><span class="name">SIZZLING TRIPLE DELIGHT</span><span>17.95</span></div><p class="desc">Sautéed sliced beef, chicken, and pork with fresh vegetables in a spicy peppercorn sauce, served on a sizzling platter.</p></div>
    <div class="entry"><div class="item"><span class="name">TRIPLE CROWN</span><span>17.95</span></div><p class="desc">Sliced tenderloin of pork, beef and chicken sautéed with assorted vegetables in a spicy garlic sauce.</p></div>
    <div class="entry"><div class="item"><span class="name">HUNAN LAMB</span><span>17.95</span></div><p class="desc">Sliced leg of lamb sautéed with water chestnuts and yellow peppers in a spicy black bean sauce.</p></div>
    <div class="entry"><div class="item"><span class="name">MONGOLIAN LAMB</span><span>17.95</span></div><p class="desc">Sliced leg of lamb stir fried with vegetables in a brown mongolian sauce.</p></div>
    <div class="entry"><div class="item"><span class="name">TANGERINE BEEF</span><span>17.95</span></div><p class="desc">Crispy chunks of steak sautéed in a spicy tangerine flavored sauce.</p></div>
    <div class="entry"><div class="item"><span class="name">SESAME BEEF</span><span>17.95</span></div><p class="desc">Crispy chunks of beef sautéed in a sweet brown sauce with a shower of sesame seeds.</p></div>
    <div class="entry"><div class="item"><span class="name">WU-XI RIBS</span><span>17.95</span></div><p class="desc">Tender Pork Ribs Sautéed In Our Sweet And Tangy Wu-Xi Sauce, Served Over A Bed Of Bok Choy</p></div>
    <div class="entry"><div class="item"><span class="name">HUNAN DUCK</span><span>19.95</span></div><p class="desc">Crispy Boneless Duck Topped With Mixed Vegetables In a Spicy Hunan Sauce</p></div>
    <div class="entry"><div class="item"><span class="name">HUNAN SHRIMP WITH WALNUTS</span><span>19.95</span></div><p class="desc">Crispy shrimp sautéed in a red spicy sauce with walnuts.</p></div>
    <div class="entry"><div class="item"><span class="name">GENERAL TSO'S SHRIMP</span><span>19.95</span></div><p class="desc">Crispy shrimp sautéed in our tangy general tso's sauce.</p></div>
    <div class="entry"><div class="item"><span class="name">TANGERINE SCALLOPS</span><span>19.95</span></div><p class="desc">Succulent Jumbo Scallops Sautéed In A Tangerine Flavored Spicy Sauce Garnished With Broccoli</p></div>
    <div class="entry"><div class="item"><span class="name">LAKE TUNG TING DUET</span><span>21.95</span></div><p class="desc">Stir-fried jumbo shrimp and sliced chicken with mixed vegetables in a delicate egg white sauce.</p></div>
    <div class="entry"><div class="item"><span class="name">HAPPY FAMILY</span><span>21.95</span></div><p class="desc">Sliced tenderloin of pork, beef, chicken, shrimp and scallops sautéed with vegetables in a brown sauce.</p></div>
  </div>

  <div class="panel">
    <div class="entry"><div class="item"><span class="name">MONGOLIAN TRIPLE FEAST</span><span>21.95</span></div><p class="desc">Sliced chicken, beef and jumbo shrimp sautéed with seasoned vegetables in our chef's Mongolian sauce.</p></div>
    <div class="entry"><div class="item"><span class="name">GENERAL TSO'S TRIPLE FRAGRANCE</span><span>21.95</span></div><p class="desc">Crispy chicken, beef and shrimp sautéed with baby corn, water chestnuts and broccoli in our tangy general tso's sauce.</p></div>
    <div class="entry"><div class="item"><span class="name">SEAFOOD SUPREME</span><span>21.95</span></div><p class="desc">Shrimp and scallops with assorted vegetables in garlic sauce.</p></div>
    <div class="entry"><div class="item"><span class="name">GOLDEN ORCHARD SHRIMP</span><span>21.95</span></div><p class="desc">Crispy jumbo shrimp sautéed with fresh fruit in a sweet golden orange glaze with cashew nuts.</p></div>
    <div class="entry"><div class="item"><span class="name">FILET MIGNON CHINESE STYLE</span><span>22.95</span></div><p class="desc">Tender filet mignon sautéed with mushrooms and onions, served in our sweet red sauce.</p></div>
    <div class="entry"><div class="item"><span class="name">GOLD COIN STEAK</span><span>22.95</span></div><p class="desc">Sliced filet mignon, sautéed with fresh vegetables in our delicious brown sauce.</p></div>
    <div class="entry"><div class="item"><span class="name">VOLCANO STEAK</span><span>22.95</span></div><p class="desc">Sliced filet mignon sautéed with mushrooms and onions in our flaming rum sauce.</p></div>
    <div class="entry"><div class="item"><span class="name">SIZZLING FILET MIGNON</span><span>22.95</span></div><p class="desc">Sliced filet mignon stir-fried with onions, mushrooms and asparagus in a spicy peppercorn sauce, served on a sizzling platter.</p></div>
    <div class="entry"><div class="item"><span class="name">SEAFOOD DELIGHT IN BIRD'S NEST</span><span>23.95</span></div><p class="desc">Lobster meat, shrimp and scallops sautéed with vegetables in a light brown sauce served in a crispy basket.</p></div>
    <div class="entry"><div class="item"><span class="name">SEAFOOD COUNTRY STYLE</span><span>23.95</span></div><p class="desc">Lobster meat, shrimp, and scallops with fresh vegetables in a tangy brown sauce, served on a sizzling hot platter.</p></div>
    <div class="entry"><div class="item"><span class="name">EMPIRE SEAFOOD COMBO</span><span>23.95</span></div><p class="desc">Jumbo shrimp, scallops, lobster and vegetables sautéed in a spicy chengdu sauce.</p></div>
    <div class="entry"><div class="item"><span class="name">SAUTÉED SEAFOOD COMBO</span><span>23.95</span></div><p class="desc">Jumbo shrimp, scallop and lobster meat sautéed in a light scallion sauce served in a hot chafing dish.</p></div>
    <div class="entry"><div class="item"><span class="name">DRAGON &amp; PHOENIX</span><span>29.95</span></div><p class="desc">Lobster meat and shrimp sautéed in a delicate white sauce on one side and chunks of crispy chicken in a brown sauce on the other.</p></div>
    <div class="entry"><div class="item"><span class="name">SURF &amp; TURF</span><span>31.95</span></div><p class="desc">Surf with lobster meat and shrimp sautéed in a white sauce &amp; turf with sliced filet mignon in brown sauce.</p></div>
  </div>
</section>

</body>
</html>
```